Business Cards and Stationery for CPA Firm
Gallowen & Company, P.C.
Business Cards and Stationery for CPA Firm -
Creative Brief
Professional
Bennett L. Gallowen
P.O. Box 482 9 West Cedar Ave. Marlow Springs, OR 97555
bgallowen@gallowencpa-example.com
www.gallowencpa-example.com
Need business cards and stationery for a CPA firm. I am open to design ideas and will provide feedback. Our generic email address for letterhead/fax is info@gallowencpa-example.com. This should be used in all locations except the business card. Each person with a business card will have his/her own email address.
Day - I've seen some with checkboxes for day of week. Other ideas welcome. Date Time Note

```html
<!DOCTYPE html>
<html lang="en">
<head>
<meta charset="utf-8">
<title>Gallowen &amp; Company, P.C. — Business Cards</title>
<link href="https://fonts.googleapis.com/css2?family=Cinzel:wght@500;600&family=Libre+Baskerville:wght@400;700&display=swap" rel="stylesheet">
<style>
  :root {
    --backdrop: #1b1c1e;
    --card-white: #fbfbfb;
    --card-grey: #e4e5e7;
    --ink-dark: #3b3e44;
    --ink-soft: #6a6d72;
    --brand-blue: #1f5b93;
    --band-top: #2b6da8;
    --band-bottom: #163f6c;
    --box-line: #8fa3b8;
    --white: #ffffff;
  }
  * { box-sizing: border-box; margin: 0; padding: 0; }
  html, body { width: 1200px; height: 871px; overflow: hidden; }
  body {
    background: var(--backdrop);
    position: relative;
    font-family: "Libre Baskerville", Georgia, serif;
  }
  .card {
    position: absolute;
    width: 560px;
    height: 320px;
    border-radius: 14px;
    overflow: hidden;
    background: linear-gradient(180deg, var(--card-white) 0%, var(--card-grey) 100%);
  }
  .card--appointment { left: 50px; top: 130px; }
  .card--contact { left: 590px; top: 420px; }

  .firm {
    position: absolute;
    display: flex;
    align-items: center;
    gap: 16px;
  }
  .firm__square {
    width: 38px; height: 38px;
    background: var(--brand-blue);
    flex: none;
  }
  .firm__name {
    font-family: "Cinzel", "Times New Roman", serif;
    font-weight: 600;
    font-size: 25px;
    color: var(--ink-dark);
    letter-spacing: 0.5px;
    white-space: nowrap;
  }
  .firm__tagline {
    position: absolute;
    font-family: "Cinzel", "Times New Roman", serif;
    font-weight: 500;
    font-size: 11px;
    letter-spacing: 2.6px;
    color: var(--brand-blue);
    text-transform: uppercase;
    white-space: nowrap;
  }

  /* Appointment card */
  .card--appointment .firm { left: 44px; top: 30px; }
  .card--appointment .firm__tagline { left: 98px; top: 72px; }
  .appointment__title {
    position: absolute; left: 130px; top: 100px;
    font-weight: 700; font-size: 19px; color: var(--brand-blue);
  }
  .field {
    position: absolute;
    font-size: 13px; color: var(--ink-soft);
    display: flex; align-items: flex-end; gap: 6px;
    white-space: nowrap;
  }
  .field__line { border-bottom: 1px solid var(--ink-soft); height: 14px; }
  .field--time { left: 240px; top: 134px; }
  .field--time .field__line { width: 180px; }
  .field--date { left: 44px; top: 160px; }
  .field--date .field__line { width: 160px; }
  .field--note { left: 44px; top: 212px; }
  .days {
    position: absolute; left: 110px; top: 196px;
    display: flex; gap: 28px;
  }
  .day { display: flex; flex-direction: column; align-items: center; gap: 5px; }
  .day__label { font-size: 10px; color: var(--ink-soft); }
  .day__box { width: 44px; height: 24px; border: 1.5px solid var(--box-line); border-radius: 3px; }

  /* Contact card */
  .card--contact .firm { left: 44px; top: 44px; }
  .card--contact .firm__tagline { left: 98px; top: 86px; }
  .contact__band {
    position: absolute; left: 0; right: 0; top: 140px; bottom: 0;
    background: linear-gradient(180deg, var(--band-top) 0%, var(--band-bottom) 100%);
  }
  .contact__notch { position: absolute; left: 0; top: 146px; }
  .contact__person {
    position: absolute; left: 40px; top: 166px;
    font-weight: 700; font-size: 19px; color: var(--white);
    white-space: nowrap;
  }
  .contact__divider {
    position: absolute; left: 298px; top: 176px; width: 1px; height: 126px;
    background: rgba(255,255,255,0.55);
  }
  .contact__list {
    position: absolute; left: 310px; top: 178px;
    list-style: none; color: var(--white);
    font-size: 10px; line-height: 15px;
    white-space: nowrap;
  }
  .contact__item { display: flex; gap: 7px; align-items: flex-start; margin-bottom: 4px; }
  .contact__item svg { flex: none; margin-top: 2px; }
</style>
</head>
<body>

<section class="card card--appointment" aria-label="Appointment card">
  <div class="firm">
    <span class="firm__square"></span>
    <span class="firm__name">Gallowen &amp; Company, P.C.</span>
  </div>
  <p class="firm__tagline">Certified Public Accountants</p>
  <h1 class="appointment__title">Appoiontment</h1>
  <div class="field field--time"><span>Time:</span><span class="field__line"></span><span>am/pm</span></div>
  <div class="field field--date"><span>Date:</span><span class="field__line"></span></div>
  <div class="field field--note"><span>Note:</span></div>
  <div class="days">
    <div class="day"><span class="day__label">Mon</span><span class="day__box"></span></div>
    <div class="day"><span class="day__label">Tues</span><span class="day__box"></span></div>
    <div class="day"><span class="day__label">Wed</span><span class="day__box"></span></div>
    <div class="day"><span class="day__label">Thu</span><span class="day__box"></span></div>
    <div class="day"><span class="day__label">Fri</span><span class="day__box"></span></div>
  </div>
</section>

<section class="card card--contact" aria-label="Business card">
  <div class="firm">
    <span class="firm__square"></span>
    <span class="firm__name">Gallowen &amp; Company, P.C.</span>
  </div>
  <p class="firm__tagline">Certified Public Accountants</p>
  <div class="contact__band"></div>
  <svg class="contact__notch" width="16" height="26" viewBox="0 0 16 26"><polygon points="0,0 14,13 0,26" fill="#fbfbfb"/></svg>
  <h2 class="contact__person">Bennett L. Gallowen</h2>
  <div class="contact__divider"></div>
  <ul class="contact__list">
    <li class="contact__item">
      <svg width="11" height="11" viewBox="0 0 12 12"><path d="M6 1 L11 6 H9.5 V11 H7 V8 H5 V11 H2.5 V6 H1 Z" fill="#fff"/></svg>
      <span>P.O. Box 482<br>9 West Cedar Ave. Marlow Springs, OR 97555</span>
    </li>
    <li class="contact__item">
      <svg width="11" height="11" viewBox="0 0 12 12"><path d="M3 1 L5 3.5 L4 5 C5 7 6 8 7.5 8.5 L9 7.5 L11 9.5 L9.5 11 C5 10.5 1.5 7 1 2.5 Z" fill="#fff"/></svg>
      <span>(555) 555-0142</span>
    </li>
    <li class="contact__item">
      <svg width="11" height="11" viewBox="0 0 12 12"><rect x="3" y="1" width="6" height="3" fill="#fff"/><rect x="1" y="4.5" width="10" height="4.5" rx="1" fill="#fff"/><rect x="3" y="8" width="6" height="3" fill="#fff"/></svg>
      <span>(555) 555-0187</span>
    </li>
    <li class="contact__item">
      <svg width="11" height="11" viewBox="0 0 12 12"><rect x="1" y="2.5" width="10" height="7" fill="none" stroke="#fff" stroke-width="1.2"/><path d="M1 2.5 L6 7 L11 2.5" fill="none" stroke="#fff" stroke-width="1.2"/></svg>
      <span>bgallowen@gallowencpa-example.com</span>
    </li>
    <li class="contact__item">
      <svg width="11" height="11" viewBox="0 0 12 12"><circle cx="6" cy="6" r="4.8" fill="none" stroke="#fff" stroke-width="1.1"/><ellipse cx="6" cy="6" rx="2" ry="4.8" fill="none" stroke="#fff" stroke-width="1"/><line x1="1.2" y1="6" x2="10.8" y2="6" stroke="#fff" stroke-width="1"/></svg>
      <span>www.gallowencpa-example.com</span>
    </li>
  </ul>
</section>

</body>
</html>
```